Pain Seminar Flyer 8.5x11

We are having a FREE seminar on Pain for our Bootcamp members at our gym. We are looking for a great looking flyer with pictures and a design to draw people in. I have attached our logo, pictures of the 2 speakers and a Word document of the flyer information needed. PLEASE PLEASE make our head shots small and in a circle like the example flyer we attached but obviously make the flyer much much nicer than the example. Also we attached pic ideas about pain.
- This must be in PSD. format WITH LAYERS and fonts so we can edit the time or reuse the flyer.
- Size 8.5x11
- Attached info. with pics and logo (along with other pics of pain!)
Thank you!
Gym

```html
<!DOCTYPE html>
<html lang="en">
<head>
<meta charset="utf-8">
<title>Free Pain Seminar Flyer</title>
<link href="https://fonts.googleapis.com/css2?family=Oswald:wght@400;500;600&family=Rubik:wght@400;500&display=swap" rel="stylesheet">
<style>
  :root {
    --ink: #2b2a2d;
    --paper: #ffffff;
    --blue: #1a6bb3;
    --blue-deep: #145a97;
    --blue-darker: #114c80;
    --blue-mid: #1d72bd;
    --blue-sky: #4a9be0;
    --blue-line: #8ec5f2;
    --list-blue: #1d6fb8;
  }
  * { margin: 0; padding: 0; box-sizing: border-box; }
  html, body { width: 950px; height: 1200px; overflow: hidden; background: var(--paper); }
  .flyer { position: relative; width: 950px; height: 1200px; overflow: hidden; background: var(--paper); font-family: "Rubik", sans-serif; }
  .backdrop { position: absolute; inset: 0; }
  .text { position: absolute; white-space: nowrap; }
  .condensed { font-family: "Oswald", sans-serif; text-transform: uppercase; }

  .brand { left: 42px; top: 30px; color: var(--ink); font-family: "Oswald", sans-serif; font-weight: 600; font-size: 40px; line-height: 44px; letter-spacing: 1px; }

  .pain-areas { right: 323px; top: 22px; text-align: right; color: var(--paper); font-weight: 500; font-size: 40px; line-height: 42px; }
  .pain-word { right: 18px; top: 8px; color: var(--blue-sky); font-weight: 500; font-size: 140px; line-height: 160px; letter-spacing: -2px; transform: scaleX(0.88); transform-origin: right center; }

  .seminar-title { left: 98px; width: 612px; top: 262px; text-align: center; color: var(--paper); font-weight: 500; font-size: 82px; line-height: 88px; letter-spacing: -1px; }
  .reserve { left: 98px; width: 612px; text-align: center; color: var(--paper); }
  .reserve-note { top: 555px; font-size: 23px; font-weight: 400; }
  .reserve-call { top: 580px; font-size: 38px; font-weight: 500; }
  .reserve-limit { top: 630px; font-size: 18px; font-weight: 400; line-height: 30px; }

  .event-date { right: 40px; top: 640px; text-align: right; color: var(--paper); font-weight: 500; }
  .event-day { font-size: 44px; line-height: 56px; }
  .event-month { font-size: 66px; line-height: 72px; letter-spacing: -1px; }
  .event-time { font-size: 56px; line-height: 64px; letter-spacing: -1px; }

  .topics { position: absolute; left: 7px; top: 740px; list-style: none; color: var(--list-blue); font-size: 22px; line-height: 30px; }
  .topics li { position: relative; padding-left: 61px; margin-bottom: 2px; }
  .topics li::before { content: ""; position: absolute; left: 0; top: 14px; width: 44px; height: 2px; background: var(--list-blue); }

  .speaker-name { color: var(--paper); font-size: 22px; line-height: 26px; }
  .speaker-cred { color: var(--paper); font-size: 13px; line-height: 18px; }
  .speaker-left { left: 65px; top: 986px; }
  .speaker-right { left: 752px; top: 934px; }

  .site { left: 42px; top: 1140px; color: var(--blue-sky); font-size: 34px; }
  .venue { right: 51px; top: 1120px; text-align: right; color: #ececec; font-size: 21px; line-height: 31px; letter-spacing: 0.5px; }
</style>
</head>
<body>
<div class="flyer">
  <svg class="backdrop" width="950" height="1200" viewBox="0 0 950 1200">
    <polygon points="399,0 950,0 950,407 708,292 404,141 399,141" fill="var(--ink)"/>
    <polygon points="404,141 708,292 950,407 950,1030 600,884 404,747" fill="var(--blue-deep)"/>
    <polygon points="708,292 950,407 950,640 713,636" fill="var(--blue-mid)"/>
    <rect x="713" y="636" width="237" height="195" fill="var(--blue-darker)"/>
    <line x1="7" y1="579" x2="950" y2="1033" stroke="var(--blue-line)" stroke-width="2"/>
    <polygon points="404,141 708,292 708,601 404,747 98,601 98,292" fill="var(--blue)" stroke="#4aa6ee" stroke-width="3"/>
    <polygon points="12,1074 551,972 950,1035 950,1200 0,1200 0,1074" fill="var(--ink)"/>
    <line x1="12" y1="1048" x2="541" y2="972" stroke="var(--blue-line)" stroke-width="3"/>
    <line x1="12" y1="1060" x2="541" y2="984" stroke="var(--blue)" stroke-width="3"/>
    <polygon points="12,977 225,977 225,1048 12,1060" fill="var(--blue)"/>
    <polygon points="700,926 938,926 938,992 700,992" fill="var(--blue)"/>
    <defs>
      <linearGradient id="photoLeft" x1="0" y1="0" x2="0" y2="1">
        <stop offset="0" stop-color="#c9ced3"/><stop offset="1" stop-color="#b98c74"/>
      </linearGradient>
      <linearGradient id="photoRight" x1="0" y1="0" x2="0" y2="1">
        <stop offset="0" stop-color="#8fa06c"/><stop offset="1" stop-color="#c9b89c"/>
      </linearGradient>
    </defs>
    <g role="img" aria-label="Portrait photo of speaker Dorian Hale">
      <polygon points="325,895 435,951 435,1064 325,1120 215,1064 215,951" fill="url(#photoLeft)" stroke="var(--blue)" stroke-width="8"/>
    </g>
    <g role="img" aria-label="Portrait photo of speaker Marcus Lindqvist">
      <polygon points="636,844 747,900 747,1013 636,1070 526,1013 526,900" fill="url(#photoRight)" stroke="var(--blue)" stroke-width="8"/>
    </g>
    <rect x="12" y="1189" width="588" height="11" fill="var(--blue)"/>
    <polygon points="600,1200 612,1189 950,1189 950,1200" fill="var(--paper)"/>
  </svg>

  <div class="text brand">COREVIA<br>BOOTCAMPS</div>

  <div class="text condensed pain-areas">Back<br>Shoulder<br>Knee</div>
  <div class="text condensed pain-word">Pain?</div>

  <h1 class="text condensed seminar-title">Free Seminar<br>On How to Stop<br>Pain</h1>
  <p class="text condensed reserve reserve-note">Reservations Required.</p>
  <p class="text condensed reserve reserve-call">Call 303-555-0172 Today</p>
  <p class="text condensed reserve reserve-limit">Limited space so don't<br>wait to sign up</p>

  <div class="text condensed event-date">
    <div class="event-day">Thursday</div>
    <div class="event-month">April 13th</div>
    <div class="event-time">7:30PM–9PM</div>
  </div>

  <ul class="topics">
    <li>How to Get Out of Pain</li>
    <li>What to do When an<br>Exercise Hurts</li>
    <li>How Exercise Helps Pain</li>
    <li>Q &amp; A to Fine Extraordinary Health</li>
  </ul>

  <div class="text speaker-left">
    <div class="speaker-name">Dorian Hale</div>
    <div class="speaker-cred">MS, CSCS, FMS</div>
  </div>
  <div class="text speaker-right">
    <div class="speaker-name">Marcus Lindqvist</div>
    <div class="speaker-cred">PT, DPT, OCS</div>
  </div>

  <div class="text site">www.Coreviafit.com</div>
  <div class="text venue">COREVIA PERSONAL TRAINING STUDIO<br>18 W. Elm St. Ridgefield, CO 80999</div>
</div>
</body>
</html>
```